Business Card Design Project

we need a business card design for our company: www.dravonix.ch
It's important to include our already existing logo (see website)

```html
<!DOCTYPE html>
<html lang="en">
<head>
<meta charset="utf-8">
<title>Dravonix – Business Card</title>
<link rel="stylesheet" href="https://fonts.googleapis.com/css2?family=Arimo:ital,wght@0,400;0,700;1,400&family=Open+Sans:wght@400;600;700&display=swap">
<style>
  :root {
    --backdrop: #2e2e2e;
    --card-white: #ffffff;
    --card-grey: #e4e4e4;
    --brand-blue: #0b72bd;
    --brand-blue-deep: #0a5fa4;
    --brand-blue-light: #7eaedd;
    --brand-blue-bright: #2a8ad0;
    --ink: #3f3f3f;
    --rule: #9a9a9a;
    --on-blue: #ffffff;
    --on-blue-soft: #e6eef6;
  }
  * { box-sizing: border-box; margin: 0; padding: 0; }
  html, body { width: 1200px; height: 900px; overflow: hidden; }
  body {
    background: var(--backdrop);
    font-family: "Arimo", Arial, sans-serif;
    position: relative;
  }
  .card {
    position: absolute;
    width: 540px;
    height: 318px;
    overflow: hidden;
    box-shadow: 0 10px 30px rgba(0,0,0,.45);
  }

  /* Front */
  .card-front {
    left: 40px; top: 140px;
    background: radial-gradient(ellipse at 35% 55%, var(--card-white) 0%, var(--card-white) 30%, var(--card-grey) 100%);
    color: var(--ink);
  }
  .front-wordmark {
    position: absolute;
    left: 48px; top: 128px;
    font-family: "Open Sans", Arial, sans-serif;
    font-weight: 700;
    font-size: 46px;
    letter-spacing: -1px;
    color: var(--brand-blue);
  }
  .divider {
    position: absolute;
    left: 318px; top: 22px;
    width: 1px; height: 240px;
    background: var(--rule);
  }
  .contact {
    position: absolute;
    left: 334px; top: 20px;
    width: 200px;
    font-size: 15px;
    line-height: 1.2;
  }
  .contact-name { color: var(--brand-blue); font-weight: 700; font-size: 19px; }
  .contact-role { font-size: 15.5px; }
  .contact-degree { font-style: italic; font-size: 11px; margin-bottom: 14px; }
  .contact-address { margin-bottom: 10px; }
  .contact-list { list-style: none; }
  .contact-list li { display: flex; align-items: center; gap: 7px; height: 19px; }
  .contact-list svg { width: 13px; height: 13px; flex: none; }
  .contact-web { color: var(--brand-blue); margin-top: 8px; font-size: 14.5px; }
  .band-main {
    position: absolute; left: 0; bottom: 0;
    width: 100%; height: 34px;
    background: var(--brand-blue);
  }
  .band-step {
    position: absolute; left: 0; bottom: 34px;
    width: 418px; height: 22px;
    background: var(--brand-blue);
  }
  .band-accent {
    position: absolute; right: 0; bottom: 34px;
    width: 112px; height: 22px;
    background: var(--brand-blue-light);
  }

  /* Back */
  .card-back {
    left: 620px; top: 440px;
    background: linear-gradient(155deg, var(--brand-blue-bright) 0%, var(--brand-blue) 45%, var(--brand-blue-deep) 100%);
    color: var(--on-blue);
    text-align: center;
  }
  .back-wordmark {
    margin-top: 78px;
    font-family: "Open Sans", Arial, sans-serif;
    font-weight: 700;
    font-size: 66px;
    letter-spacing: -1px;
    line-height: 1;
  }
  .back-tagline {
    margin-top: 14px;
    font-family: "Open Sans", Arial, sans-serif;
    font-size: 15px;
    letter-spacing: 1px;
    text-transform: uppercase;
    color: var(--on-blue-soft);
  }
  .back-web {
    margin-top: 54px;
    font-size: 17px;
    letter-spacing: 7px;
    color: var(--on-blue-soft);
  }
</style>
</head>
<body>

<section class="card card-front" aria-label="Card front">
  <div class="front-wordmark">Dravonix</div>
  <div class="divider"></div>
  <div class="contact">
    <p class="contact-name">Mara Keller</p>
    <p class="contact-role">Managing Partner</p>
    <p class="contact-degree">MSc in Information Technology</p>
    <p class="contact-address">Lindenweg 12<br>CH-8004 Zürich<br>Switzerland</p>
    <ul class="contact-list">
      <li>
        <svg viewBox="0 0 16 16" aria-hidden="true"><path fill="#0b72bd" d="M3.5 1.5l2.5 0 1 3.5-1.7 1.2a8 8 0 0 0 4.5 4.5l1.2-1.7 3.5 1v2.5c0 .8-.7 1.5-1.5 1.5A12 12 0 0 1 2 3c0-.8.7-1.5 1.5-1.5z"/></svg>
        +41 79 210 47 63
      </li>
      <li>
        <svg viewBox="0 0 16 16" aria-hidden="true"><circle cx="8" cy="8" r="7" fill="#0b72bd"/></svg>
        dravonix.ch
      </li>
      <li>
        <svg viewBox="0 0 16 16" aria-hidden="true"><rect x="1" y="3" width="14" height="10" fill="none" stroke="#0b72bd" stroke-width="1.6"/><path d="M1 3l7 6 7-6" fill="none" stroke="#0b72bd" stroke-width="1.6"/></svg>
        mara.keller@dravonix.ch
      </li>
      <li class="contact-web">
        <svg viewBox="0 0 16 16" aria-hidden="true"><circle cx="8" cy="8" r="6.5" fill="none" stroke="#0b72bd" stroke-width="1.4"/><ellipse cx="8" cy="8" rx="3" ry="6.5" fill="none" stroke="#0b72bd" stroke-width="1.2"/><path d="M1.5 8h13" stroke="#0b72bd" stroke-width="1.2"/></svg>
        www.dravonix.ch
      </li>
    </ul>
  </div>
  <div class="band-step"></div>
  <div class="band-accent"></div>
  <div class="band-main"></div>
</section>

<section class="card card-back" aria-label="Card back">
  <div class="back-wordmark">Dravonix</div>
  <p class="back-tagline">Enterprise Software Studio</p>
  <p class="back-web">www.dravonix.ch</p>
</section>

</body>
</html>
```